Layout für Broschüre für chemiefreie Lösung, Kühlwasser aufzubereiten
Zielgruppe
VELTROMAX hat eine Technologie entwickelt, die in der Industrie eingesetzt wird um in geschlossenen und offenen Kühlkreisläufen ohne Biozide und Korrosion Inhibitoren das Kühlwasser aufzubereiten. Mit VELTROMAX haben die Unternehmen eine chemiefreie Lösungen gegen Biofouling, Korrosion und Kalk. Zielgruppe sind alle Unternehmen die etwas produzieren oder Klimaanlagen / Heizungssysteme betreiben. Es geht um zukunftsorientierte und vor allem nachhaltige Technologie ohne Einsatz von Chemie.
Aufgabenstellung
Wir suchen für die Broschüre ein neues Layout, dass geradlinig und klar strukturiert ist, vor allem modern. Die Broschüre sollte DIN A 4 - Format sein in der gewohnten Struktur Umschlagseite innen und außen und 8 - 10 Innenseiten. Im Layout sollte ein roter Faden zu erkennen sein, aber nicht jede Seite gleich aussehen. Die Anlagen sind nur beispielhaft vom bestehenden Material und sollten vom Layout keinesfalls eine Orientierung geben, denn das soll verändert werden. Die Anlagen sind für einen inhaltlichen Überblick.

```html
<!DOCTYPE html>
<html lang="de">
<head>
<meta charset="utf-8">
<title>VELTROMAX – Broschüre Umschlag</title>
<link rel="stylesheet" href="https://fonts.googleapis.com/css2?family=Roboto:wght@300;400;500;700&display=swap">
<style>
  :root {
    --canvas: #cfcfcf;
    --paper: #e9e9e8;
    --paper-light: #efefee;
    --ink: #2b2b2b;
    --ink-soft: #6a6a6a;
    --accent-green: #5cbf3c;
    --photo-dark: #1c1c1c;
    --photo-mid: #4a4a4a;
    --photo-light: #8a8a8a;
    --white: #ffffff;
  }
  * { margin: 0; padding: 0; box-sizing: border-box; }
  html, body {
    width: 1200px;
    height: 900px;
    overflow: hidden;
    background: var(--canvas);
    font-family: "Roboto", Arial, sans-serif;
  }
  .spread {
    position: absolute;
    left: 63px;
    top: 70px;
    width: 1074px;
    height: 760px;
    display: flex;
    box-shadow: 0 12px 30px rgba(0,0,0,0.18);
  }
  .page {
    position: relative;
    width: 537px;
    height: 760px;
    background: var(--paper);
    overflow: hidden;
  }
  /* Back cover */
  .back-cover { background: linear-gradient(90deg, var(--paper-light), var(--paper)); }
  .back-cover__content {
    position: absolute;
    left: 54px;
    bottom: 70px;
    width: 240px;
  }
  .back-cover__headline {
    color: var(--accent-green);
    font-weight: 700;
    font-size: 12px;
    line-height: 1.2;
    margin-bottom: 4px;
  }
  .back-cover__body {
    color: var(--ink-soft);
    font-size: 6.5px;
    line-height: 1.45;
    margin-bottom: 14px;
  }
  /* Front cover */
  .front-cover__photo {
    position: absolute;
    left: 0; top: 0;
    width: 100%;
    height: 470px;
    background:
      radial-gradient(ellipse 55% 40% at 62% 30%, var(--photo-light) 0%, transparent 70%),
      linear-gradient(160deg, var(--photo-mid) 0%, var(--photo-dark) 85%);
  }
  .front-cover__title {
    position: absolute;
    left: 40px;
    top: 352px;
    color: var(--white);
    font-weight: 300;
    font-size: 30px;
    line-height: 1.1;
    letter-spacing: 0.5px;
    text-transform: uppercase;
  }
  .front-cover__rule {
    position: absolute;
    left: 40px;
    top: 432px;
    width: 240px;
    height: 3px;
    background: var(--accent-green);
  }
  .front-cover__subtitle {
    position: absolute;
    left: 40px;
    top: 505px;
    color: var(--ink);
    font-size: 12px;
    letter-spacing: 2px;
    text-transform: uppercase;
  }
  .brand-mark {
    display: flex;
    align-items: center;
    gap: 5px;
    color: var(--accent-green);
    font-weight: 500;
    font-size: 12px;
    letter-spacing: 0.5px;
  }
  .brand-mark__dot {
    width: 8px; height: 8px;
    border-radius: 50%;
    background: var(--accent-green);
  }
  .front-cover__brand {
    position: absolute;
    right: 50px;
    top: 600px;
  }
</style>
</head>
<body>
  <main class="spread">
    <section class="page back-cover" aria-label="Umschlag hinten">
      <div class="back-cover__content">
        <h2 class="back-cover__headline">Klares Wasser ohne jede Chemie</h2>
        <p class="back-cover__body">Nachhaltige Kühlwasseraufbereitung für Industrie, Klimaanlagen und Heizungssysteme. Wirksam gegen Biofouling, Korrosion und Kalk – ganz ohne Biozide und Inhibitoren.</p>
        <div class="brand-mark"><span class="brand-mark__dot"></span>VELTROMAX</div>
      </div>
    </section>

    <section class="page front-cover" aria-label="Umschlag vorne">
      <div class="front-cover__photo" role="img" aria-label="Schwarzweißfoto: Wasser spritzt auf eine geöffnete Hand"></div>
      <h1 class="front-cover__title">Chemiefreie<br>Wasserbehandlung</h1>
      <div class="front-cover__rule"></div>
      <p class="front-cover__subtitle">Lorem ipsum dolores</p>
      <div class="brand-mark front-cover__brand"><span class="brand-mark__dot"></span>VELTROMAX</div>
    </section>
  </main>
</body>
</html>
```